Income Tax Flyer - Updates Needed

Just need to update this flyer design and give it a new look. We would like to keep all the same wording but make it stand out a little more. Our selling point is the "Same Day Tax Advance up to $6,000"

Industry/Entity Type

Lending, Small Loans, Tax Services, Title Loans, Personal Loans

```html
<!DOCTYPE html>
<html lang="en">
<head>
<meta charset="utf-8">
<title>Same Day Tax Advance Flyer</title>
<link rel="stylesheet" href="https://fonts.googleapis.com/css2?family=Montserrat:wght@500;600;700;800;900&display=swap">
<style>
  :root {
    --backdrop: #b3b3b3;
    --paper: #ffffff;
    --brand-red: #c8111c;
    --brand-green: #00522a;
    --lime: #bcd400;
    --ink-white: #ffffff;
  }
  * { margin: 0; padding: 0; box-sizing: border-box; }
  html, body {
    width: 1200px; height: 1117px; overflow: hidden;
    background: var(--backdrop);
    font-family: "Montserrat", sans-serif;
  }
  .flyer {
    position: absolute; left: 272px; top: 42px;
    width: 657px; height: 1032px;
    background: var(--paper); overflow: hidden;
  }
  .hero-photo {
    position: absolute; left: 0; top: 0; width: 657px; height: 380px;
    background:
      linear-gradient(to bottom, rgba(255,255,255,0) 60%, #ffffff 100%),
      radial-gradient(ellipse 150px 190px at 410px 230px, #9fb6d6 0%, #c4d2e6 55%, rgba(230,235,242,0) 100%),
      linear-gradient(100deg, #e7e4df 0%, #f6f6f5 30%, #eeeff1 65%, #d9d9d9 100%);
  }
  .brand {
    position: absolute; left: 55px; top: 112px; width: 250px;
    text-align: center; color: var(--brand-red);
    font-weight: 800; font-size: 27px; line-height: 32px; letter-spacing: -0.3px;
  }
  .headline {
    position: absolute; left: 0; width: 657px; top: 372px;
    text-align: center; font-weight: 900; line-height: 57px;
    font-size: 60px; letter-spacing: -0.5px; color: var(--brand-green);
  }
  .headline .accent { color: var(--brand-red); }
  .amount {
    position: absolute; left: 0; width: 657px; top: 486px;
    text-align: center; font-weight: 900; font-size: 120px;
    line-height: 130px; letter-spacing: -2px; color: var(--brand-red);
  }
  .tagline {
    position: absolute; left: 0; width: 657px; top: 628px;
    text-align: center; font-weight: 500; font-size: 38.5px;
    line-height: 43px; color: var(--brand-green);
  }
  .tagline strong { font-weight: 800; color: var(--brand-red); }
  .footer-shape { position: absolute; left: 0; top: 760px; }
  .benefits {
    position: absolute; left: 58px; top: 732px; width: 540px; height: 129px;
    background: linear-gradient(135deg, #b80e17 0%, var(--brand-red) 20%);
    border: 2px solid #ffffff; border-radius: 14px;
    box-shadow: 0 4px 0 #003b1e;
    display: flex; justify-content: space-around; padding: 8px 14px 0;
  }
  .benefit { width: 170px; text-align: center; color: var(--ink-white); }
  .benefit svg { display: block; margin: 0 auto; }
  .benefit-label { font-size: 14px; font-weight: 800; line-height: 15px; margin-top: 8px; }
  .contact-heading {
    position: absolute; left: 62px; width: 533px; top: 878px;
    display: flex; align-items: center; gap: 10px;
    color: var(--lime); font-weight: 800; font-size: 23px; white-space: nowrap;
  }
  .contact-heading::before, .contact-heading::after {
    content: ""; flex: 1; height: 1px; background: #ffffff; opacity: .8;
  }
  .phone {
    position: absolute; left: 0; width: 657px; top: 908px;
    display: flex; justify-content: center; align-items: center; gap: 14px;
    color: var(--ink-white); font-weight: 800; font-size: 54px; letter-spacing: -1px;
  }
  .locations {
    position: absolute; left: 55px; top: 974px; width: 560px;
    display: flex; justify-content: space-between;
  }
  .location {
    display: flex; gap: 8px; color: var(--ink-white);
    font-size: 12.2px; font-weight: 500; line-height: 15px;
  }
  .location + .location { border-left: 1px solid var(--lime); padding-left: 18px; }
  .location svg { flex: none; margin-top: 1px; }
</style>
</head>
<body>
<main class="flyer">
  <div class="hero-photo" role="img" aria-label="Photo of a smiling woman at a desk with a laptop, checking her phone in a bright office"></div>

  <div class="brand">Harborline Lending</div>

  <h1 class="headline"><span class="accent">SAME DAY</span> TAX<br>ADVANCE UP TO</h1>
  <div class="amount">$6,000</div>
  <p class="tagline">File your takes and apply<br>for an <strong>Easy Advance!</strong></p>

  <svg class="footer-shape" width="657" height="272" viewBox="0 0 657 272">
    <path d="M0 0 Q328 70 657 0 L657 45 Q328 110 0 45 Z" fill="var(--lime)"/>
    <path d="M0 47 Q328 112 657 47 L657 272 L0 272 Z" fill="#ffffff"/>
    <path d="M0 52 Q328 117 657 52 L657 272 L0 272 Z" fill="var(--brand-green)"/>
  </svg>

  <section class="benefits">
    <div class="benefit">
      <svg width="68" height="68" viewBox="0 0 68 68" fill="none" stroke="#fff" stroke-width="2">
        <circle cx="34" cy="34" r="32"/>
        <circle cx="34" cy="36" r="17"/>
        <path d="M31 15h6M34 15v4"/>
        <text x="34" y="43" text-anchor="middle" font-family="Montserrat, sans-serif" font-weight="800" font-size="20" fill="#fff" stroke="none">$</text>
      </svg>
      <div class="benefit-label">AVAILABLE IN<br>24 HOURS OR LESS</div>
    </div>
    <div class="benefit">
      <svg width="68" height="68" viewBox="0 0 68 68" fill="none" stroke="#fff" stroke-width="2">
        <circle cx="34" cy="34" r="32"/>
        <rect x="22" y="14" width="20" height="38" rx="3"/>
        <path d="M27 25h8M27 31h8M27 37h6"/>
        <circle cx="43" cy="32" r="7"/>
        <text x="43" y="36" text-anchor="middle" font-family="Montserrat, sans-serif" font-weight="700" font-size="10" fill="#fff" stroke="none">$</text>
      </svg>
      <div class="benefit-label">CHOOSE YOUR<br>LOAN AMOUNT</div>
    </div>
    <div class="benefit">
      <svg width="68" height="68" viewBox="0 0 68 68" fill="none" stroke="#fff" stroke-width="2">
        <circle cx="34" cy="34" r="32"/>
        <circle cx="37" cy="20" r="8"/>
        <text x="37" y="24" text-anchor="middle" font-family="Montserrat, sans-serif" font-weight="700" font-size="11" fill="#fff" stroke="none">$</text>
        <path d="M14 46l8-8h10l12-6c3-1 5 2 3 4l-13 12H20z"/>
      </svg>
      <div class="benefit-label">QUICK AND<br>EASY</div>
    </div>
  </section>

  <h2 class="contact-heading">CONTACT US TODAY!</h2>

  <div class="phone">
    <svg width="40" height="40" viewBox="0 0 40 40">
      <circle cx="20" cy="20" r="20" fill="var(--lime)"/>
      <path d="M13 10c1-1 3-1 4 0l2 4c0 1 0 2-1 3l-1 1c1 3 3 5 6 6l1-1c1-1 2-1 3-1l4 2c1 1 1 3 0 4l-2 2c-8 1-18-9-17-17z" fill="var(--brand-green)"/>
    </svg>
    <span>123-456-7890</span>
  </div>

  <div class="locations">
    <div class="location">
      <svg width="12" height="15" viewBox="0 0 12 15"><path d="M6 0a6 6 0 0 1 6 6c0 4-6 9-6 9S0 10 0 6a6 6 0 0 1 6-6z" fill="var(--lime)"/><circle cx="6" cy="6" r="2.2" fill="var(--brand-green)"/></svg>
      <span>Street Name, Street<br>Address City State Zip</span>
    </div>
    <div class="location">
      <svg width="12" height="15" viewBox="0 0 12 15"><path d="M6 0a6 6 0 0 1 6 6c0 4-6 9-6 9S0 10 0 6a6 6 0 0 1 6-6z" fill="var(--lime)"/><circle cx="6" cy="6" r="2.2" fill="var(--brand-green)"/></svg>
      <span>Street Name, Street<br>Address City State Zip</span>
    </div>
    <div class="location">
      <svg width="12" height="15" viewBox="0 0 12 15"><path d="M6 0a6 6 0 0 1 6 6c0 4-6 9-6 9S0 10 0 6a6 6 0 0 1 6-6z" fill="var(--lime)"/><circle cx="6" cy="6" r="2.2" fill="var(--brand-green)"/></svg>
      <span>Street Name, Street<br>Address City State Zip</span>
    </div>
  </div>
</main>
</body>
</html>
```